Young Balance Support Network

We need a poster explaining that some children live with a disability called Vestibular Disorder. Feel free to ask question. We want you to respect our color code, same as our logo.

Here is our website : http://www.ybsnetwork.org/

We need to sensibilise people about this disability for children.

Industry/Entity Type

Charity

Font styles to use
Serif

Requirements
Must have
• 1. our logo (with all our details) + one of the photo of Marek
• 2. design showing a child with a dizziness for exemple
• 3. a title saying : Aidez-nous à changer la vie des enfants vivant avec un problème vestibulaire
• 4.include the text attached (information flyer YBSN)
• Poster size : 24"X 36"
Should not have
• wheel chair

```html
<!DOCTYPE html>
<html lang="fr">
<head>
<meta charset="utf-8">
<title>YBSN – Affiche de sensibilisation</title>
<link rel="stylesheet" href="https://fonts.googleapis.com/css2?family=Roboto+Slab:wght@400;700&family=Roboto:wght@400;500&display=swap">
<style>
  :root{
    --sky:#56c1ee;
    --sun:#f8b22b;
    --lime:#c4d32e;
    --mist:#ebe9ea;
    --ink:#5a5a5a;
    --title:#f5a922;
    --white:#ffffff;
    --stage:#d9d9d9;
  }
  *{box-sizing:border-box;margin:0;padding:0}
  html,body{width:1200px;height:1200px;overflow:hidden}
  body{background:var(--stage);font-family:"Roboto",sans-serif;position:relative}
  .poster{position:absolute;left:240px;top:60px;width:720px;height:1080px;background:var(--white);box-shadow:0 4px 14px rgba(0,0,0,.25);overflow:hidden}
  .side{position:absolute;left:0;top:0;width:252px;height:1080px}
  .stripe{position:absolute;top:0;height:10px;width:84px}
  .stripe--sky{left:0;background:var(--sky)}
  .stripe--sun{left:84px;background:var(--sun)}
  .stripe--lime{left:168px;background:var(--lime)}
  .brand{position:absolute;top:10px;left:0;width:252px;height:205px;display:flex;align-items:center;justify-content:center;gap:10px}
  .brand__dot{width:26px;height:26px;border-radius:50%;background:var(--sky)}
  .brand__name{font-family:"Roboto Slab",serif;font-size:34px;color:var(--lime);letter-spacing:3px}
  .panel{position:absolute;left:0;width:252px;padding:0 20px}
  .panel h2{font-family:"Roboto Slab",serif;font-weight:400;line-height:1.3}
  .panel p{font-size:13px;line-height:19px;padding-left:2px}
  .panel--vestibule{top:215px;height:145px;background:var(--sky);color:var(--white);padding-top:24px}
  .panel--vestibule h2{font-size:15.5px;font-weight:700;margin-bottom:14px}
  .panel--areflexie{top:360px;height:196px;background:var(--mist);color:var(--ink);padding-top:30px}
  .panel--areflexie h2{font-size:15.5px;margin-bottom:14px;line-height:22px}
  .panel--consequences{top:556px;height:524px;background:var(--lime);color:var(--white);padding-top:24px}
  .panel--consequences h2{font-size:18px;line-height:22px;margin-bottom:14px;max-width:190px}
  .panel--consequences p{margin-bottom:5px}
  .hero{position:absolute;left:252px;top:0;width:468px;height:655px;background:linear-gradient(160deg,#6f6467 0%,#8a6f69 45%,#3a3236 75%,#1f1b1d 100%)}
  .hero h1{position:absolute;left:18px;top:462px;font-family:"Roboto Slab",serif;font-weight:700;color:var(--title);line-height:1}
  .hero__big{display:block;font-size:50px;margin-bottom:14px}
  .hero__rest{display:block;font-size:29px;line-height:36px}
  .mission{position:absolute;left:252px;top:655px;width:468px;height:225px;background:var(--sky);color:var(--white);padding:30px 18px 0 20px}
  .mission h2{font-family:"Roboto Slab",serif;font-size:15.5px;font-weight:700;margin-bottom:18px}
  .mission p{font-size:13px;line-height:19px}
  .portrait{position:absolute;left:252px;top:880px;width:236px;height:200px;background:radial-gradient(circle at 45% 45%,#f1c89a 0%,#e6a874 45%,#d0463c 80%,#f4efe8 100%)}
  .contact{position:absolute;right:16px;top:880px;width:232px;text-align:right;font-family:"Roboto Slab",serif}
  .contact__org{margin-top:25px;font-size:16px;line-height:23px;color:var(--lime)}
  .contact__web{margin-top:12px;font-size:12px;line-height:21px;color:var(--sky);letter-spacing:1px}
  .contact__ccp{font-size:11.5px;line-height:21px;color:var(--sky)}
  .social{margin-top:12px;display:flex;justify-content:flex-end;align-items:center;gap:6px;font-size:13px;color:var(--sky)}
  .social__mark{width:16px;height:16px;background:var(--sky)}
</style>
</head>
<body>
<main class="poster">
  <aside class="side">
    <span class="stripe stripe--sky"></span>
    <span class="stripe stripe--sun"></span>
    <span class="stripe stripe--lime"></span>
    <div class="brand">
      <span class="brand__dot"></span>
      <span class="brand__name">YBSN</span>
    </div>
    <section class="panel panel--vestibule">
      <h2>Qu’est-ce que le vestibule ?</h2>
      <p>C’est un organe sensoriel, pilier de votre équilibre, véritable 6ème sens situé dans l’oreille interne.</p>
    </section>
    <section class="panel panel--areflexie">
      <h2>Qu’est ce qu’une aréflexie vestibulaire ?</h2>
      <p>C’est l’absence complète de toute information vestibulaire. L’enfant a ainsi l’impression que tout vacille autour de lui, jour et nuit.</p>
    </section>
    <section class="panel panel--consequences">
      <h2>Quelles en sont les conséquences pour l’enfant ?</h2>
      <p>Le développement moteur de l’enfant est retardé car il doit trouver des solutions afin de construire son équilibre, stabiliser son regard et son corps.</p>
      <p>Certains apprentissages sont de véritables obstacles pour l’enfant : se représenter son propre corps, se situer dans l’espace qui l’entoure, interagir avec les autres, communiquer, écrire, lire, manger, boire, marcher. Chacune de ces actions necessitent des efforts considérables pour se concentrer quelques secondes ou minutes.</p>
      <p>Quand l’enfant réussit à effectuer l’une de ces actions, son comportement peut sembler déroutant et bien trop souvent mal interprété par le grand public.</p>
    </section>
  </aside>

  <section class="hero" role="img" aria-label="Photo d’un enfant pris de vertiges, les mains sur la tête">
    <h1><span class="hero__big">AIDEZ-NOUS</span><span class="hero__rest">À CHANGER LA VIE DES<br>ENFANTS VIVANT AVEC UN<br>PROBLÈME VESTIBULAIRE</span></h1>
  </section>

  <section class="mission">
    <h2>Quel est le but de notre association ?</h2>
    <p>Notre association a pour but de promouvoir les troubles vestibulaires chez l’enfant, ses conséquences sur sa santé ainsi que celui de son entourage et de soutenir ces enfants et leurs parents en leur offrant un espace de parole et des solutions concrètes pour soulager leur quotidien. Notre association a également pour but de financer et promouvoir toute action de recherche scientifique visant à aider les enfants ayant un trouble vestibulaire.</p>
  </section>

  <div class="portrait" role="img" aria-label="Photo d’un bébé portant des lunettes, assis dans un siège rouge"></div>

  <footer class="contact">
    <p class="contact__org">YOUNG BALANCE SUPPORT<br>NETWORK</p>
    <p class="contact__web">WWW.YBSNETWORK.ORG<br>INFO@YBSNETWORK.ORG</p>
    <p class="contact__ccp">CCP: 12-458730-6</p>
    <div class="social"><span class="social__mark"></span><span>ybsnetwork</span></div>
  </footer>
</main>
</body>
</html>
```